Where the Morning Went: A Season of Turning

The book size is 6x9. I am more interested in an illustrative design like the one I have posted below with a picture of my face and then having elements in the background of a barn, a cross and my little girls eyes peaking out from behind the scenery.
"Where the Morning Went… A Season of Turning" is a gripping memoir of resilience, faith, and courage. Marlene Kostrova’s journey pulls back the curtain on a ranch family fractured by addiction, abuse, and chaos, while revealing an extraordinary path to self-discovery and purpose.
Marlene, her older sister Bettina, and their three younger brothers grow up in a destabilizing environment where frequent moves and changing schools are routine. All the while, they navigate life in the shadow of their father’s addiction, schizophrenia, and violent outbursts. With dark secrets of sexual abuse and domestic violence lurking behind closed doors, the family seems trapped in a cycle of destruction.
Yet, Marlene’s spirit remains unbroken. Anchored by her unshakable belief that God is her true father and Jesus her brother, she clings to her faith and a guiding philosophy she calls “the next right move”—a quiet force that propels her forward, even as those around her fall victim to their demons. As her siblings descend into addiction, incarceration, and heartbreak, Marlene works to protect herself from the same fate while holding onto the family she cherishes.
Described by those who know her as possessing sophisticated grit, Marlene rises above her circumstances with a unique blend of resilience, conscientiousness, and inner grace. She is driven by her belief in “organic truth”—the truth you possess before you are even born—which, once discovered, has the power to set you free into becoming who you were met to be. This profound conviction, along with her commitment to “the next right move,” guides her through life’s darkest moments.
Armed with a PhD in Human Science and experience as a child abuse and neglect investigator, therapist, professor, business leader and coach, Marlene’s true triumph lies in something far deeper: surviving three near-death experiences and realizing that her purpose transcends personal, professional, and material achievements. Rather than pursuing happiness, she dedicates herself to uncovering meaning.
In this inspiring and candid memoir, she invites readers on a journey of becoming—one marked by faith, perseverance, and the courage to listen to the voice of organic truth within. Her story is a testament to the resilience of the human spirit and a beacon of hope for anyone navigating their own path to reclaim their sense of self, purpose, and freedom.

```html
<!DOCTYPE html>
<html lang="en">
<head>
<meta charset="utf-8">
<title>Where the Morning Went: A Season of Turning — Book Cover</title>
<link rel="stylesheet" href="https://fonts.googleapis.com/css2?family=Crimson+Pro:ital,wght@0,400;0,600;1,400&display=swap">
<style>
  :root {
    --page: #ffffff;
    --cover: #5a0006;
    --accent: #f98c22;
    --accent-deep: #c8520f;
    --ink: #ffffff;
  }
  * { margin: 0; padding: 0; box-sizing: border-box; }
  html, body {
    width: 1200px;
    height: 1000px;
    overflow: hidden;
    background: var(--page);
  }
  .canvas {
    position: relative;
    width: 1200px;
    height: 1000px;
  }
  .cover {
    position: absolute;
    left: 300px;
    top: 50px;
    width: 600px;
    height: 900px;
    background: var(--cover);
    color: var(--ink);
    font-family: "Crimson Pro", Georgia, serif;
    overflow: hidden;
  }
  .tagline {
    position: absolute;
    top: 46px;
    left: 0;
    width: 100%;
    text-align: center;
    font-style: italic;
    font-size: 19px;
    letter-spacing: 0.2px;
  }
  .figure-art {
    position: absolute;
    left: 180px;
    top: 100px;
    width: 240px;
    height: 575px;
  }
  .title {
    position: absolute;
    top: 195px;
    left: 0;
    width: 100%;
    text-align: center;
    font-weight: 600;
    font-size: 78px;
    line-height: 100px;
    letter-spacing: -1px;
    text-transform: uppercase;
  }
  .title span { display: block; }
  .subtitle {
    position: absolute;
    top: 683px;
    left: 0;
    width: 100%;
    text-align: center;
    font-size: 25px;
  }
  .divider-mark {
    position: absolute;
    left: 268px;
    top: 730px;
    width: 70px;
    height: 50px;
  }
  .author {
    position: absolute;
    top: 793px;
    left: 0;
    width: 100%;
    text-align: center;
    font-size: 30px;
    letter-spacing: 5px;
    text-transform: uppercase;
  }
</style>
</head>
<body>
<main class="canvas">
  <section class="cover">
    <p class="tagline">A gripping memoir of resilience, faith, and courage</p>

    <svg class="figure-art" viewBox="0 0 240 575" role="img" aria-label="Illustration of a woman's silhouette in orange, tangled in loose red scribbled lines">
      <defs>
        <radialGradient id="figureGlow" cx="50%" cy="45%" r="60%">
          <stop offset="0%" stop-color="var(--accent)"/>
          <stop offset="70%" stop-color="var(--accent-deep)" stop-opacity="0.75"/>
          <stop offset="100%" stop-color="var(--cover)" stop-opacity="0"/>
        </radialGradient>
      </defs>
      <rect x="0" y="0" width="240" height="575" rx="110" fill="url(#figureGlow)"/>
    </svg>

    <h1 class="title">
      <span>Where</span>
      <span>the</span>
      <span>Morning</span>
      <span>Went</span>
    </h1>

    <p class="subtitle">A Season of Turning</p>

    <svg class="divider-mark" viewBox="0 0 70 50" role="img" aria-label="Small orange decorative mark">
      <rect x="5" y="5" width="60" height="40" rx="18" fill="var(--accent)"/>
    </svg>

    <p class="author">Marlene Kostrova</p>
  </section>
</main>
</body>
</html>
```